Design a business card & stationary for a mortgage company

We are looking for a good looking business card design for our mortgage company that includes our logo. We received a free design as part of our logo project but we don't love it. The company is called "Pinecrest Mortgage Company" so we like waves and lighthouses. The logo should be included. We have a version in both vertical and horizontal that we have provided.

Industry/Entity Type

Finance

Contact Information for Business Card

This should include our new logo file

Requirements
Must have
• 3. The details you'd like on the card - name, title, phone, email, website, address, social media handles etc.
1. Marcus Hale
Vice President
555-419-6253
Fax 888-304-2918
mhale@pinecrestmortgage.example
NMLS 47162 - Company NMLS 61290
18 Larkin Ave
Alder Cove, DE 08614

```html
<!DOCTYPE html>
<html lang="en">
<head>
<meta charset="utf-8">
<title>Pinecrest Mortgage Company – Business Card</title>
<link href="https://fonts.googleapis.com/css2?family=Open+Sans:ital,wght@0,400;0,600;0,700;1,400&display=swap" rel="stylesheet">
<style>
  :root {
    --brand-blue: #135d9a;
    --name-blue: #0a86d6;
    --navy: #1d2a6e;
    --paper: #ffffff;
    --backdrop: #2b2f35;
  }
  * { box-sizing: border-box; margin: 0; padding: 0; }
  html, body {
    width: 1200px; height: 900px; overflow: hidden;
    background: var(--backdrop);
    font-family: "Open Sans", Arial, sans-serif;
  }
  .sheet {
    position: relative; width: 1200px; height: 900px;
    display: flex; flex-direction: column; align-items: center; justify-content: center; gap: 56px;
  }
  .card {
    position: relative; width: 640px; height: 366px;
    background: var(--paper); overflow: hidden;
    box-shadow: 0 10px 30px rgba(0,0,0,.35);
  }

  /* ---------- Back of card ---------- */
  .card-back .brand-mark {
    position: absolute; left: 0; right: 0; top: 92px;
    text-align: center; color: var(--brand-blue);
    font-weight: 700; font-size: 30px; line-height: 1.15;
  }
  .card-back .brand-mark .brand-dot {
    display: inline-block; width: 18px; height: 18px; border-radius: 50%;
    background: var(--brand-blue); margin-right: 10px; vertical-align: 2px;
  }
  .card-back .web-band {
    position: absolute; left: 0; right: 0; top: 236px; height: 72px;
    background: var(--brand-blue);
    display: flex; align-items: center; justify-content: center;
    color: var(--paper); font-size: 30px; font-weight: 400; letter-spacing: .2px;
  }

  /* ---------- Front of card ---------- */
  .card-front .corner-wedge { position: absolute; left: 0; top: 0; }
  .card-front .brand-mark {
    position: absolute; left: 92px; top: 46px; width: 240px;
    color: var(--brand-blue); font-weight: 700; font-size: 22px; line-height: 1.2;
  }
  .card-front .holder {
    position: absolute; right: 34px; top: 44px; text-align: right;
  }
  .holder .holder-name {
    color: var(--name-blue); font-weight: 700; font-size: 40px; line-height: 1.1;
  }
  .holder .holder-title {
    display: inline-block; margin-top: 2px; padding: 0 6px 6px 40px;
    color: var(--navy); font-style: italic; font-size: 17px;
    border-bottom: 3px solid var(--navy);
  }
  .contact-panel {
    position: absolute; left: 286px; right: 0; top: 176px; bottom: 0;
    background: var(--brand-blue);
    clip-path: polygon(44px 0, 100% 0, 100% 100%, 0 100%);
    padding: 6px 0 0 0;
  }
  .contact-row {
    display: flex; align-items: center;
    border-bottom: 2px solid var(--paper);
    height: 32px; color: var(--paper); font-size: 14px;
  }
  .contact-row.address { height: 58px; align-items: flex-start; padding-top: 6px; border-bottom: none; line-height: 1.35; }
  .contact-row .icon-cell {
    width: 70px; height: 100%; flex: none;
    display: flex; align-items: center; justify-content: flex-end; padding-right: 14px;
    border-right: 2px solid var(--paper);
  }
  .contact-row.address .icon-cell { align-items: flex-start; }
  .contact-row .value { padding-left: 14px; }
</style>
</head>
<body>
<main class="sheet">

  <section class="card card-back" aria-label="Business card back">
    <div class="brand-mark"><span class="brand-dot"></span>Pinecrest<br>Mortgage Company</div>
    <div class="web-band">mhalepinecrestmortgage.example</div>
  </section>

  <section class="card card-front" aria-label="Business card front">
    <svg class="corner-wedge" width="200" height="200" viewBox="0 0 200 200" aria-hidden="true">
      <polygon points="0,0 70,0 0,150" fill="var(--brand-blue)"/>
    </svg>
    <div class="brand-mark">Pinecrest Mortgage Company</div>

    <div class="holder">
      <div class="holder-name">Marcus Hale</div>
      <div class="holder-title">Vice President</div>
    </div>

    <div class="contact-panel">
      <div class="contact-row">
        <div class="icon-cell">
          <svg width="16" height="16" viewBox="0 0 24 24" aria-label="Phone"><path fill="#fff" d="M6.6 10.8a15 15 0 0 0 6.6 6.6l2.2-2.2c.3-.3.7-.4 1-.2 1.1.4 2.3.6 3.6.6.6 0 1 .4 1 1V20c0 .6-.4 1-1 1A17 17 0 0 1 3 4c0-.6.4-1 1-1h3.5c.6 0 1 .4 1 1 0 1.3.2 2.5.6 3.6.1.3 0 .7-.2 1z"/></svg>
        </div>
        <div class="value">555-419-6253</div>
      </div>
      <div class="contact-row">
        <div class="icon-cell">
          <svg width="18" height="16" viewBox="0 0 24 22" aria-label="Fax"><path fill="none" stroke="#fff" stroke-width="2" d="M6 8V2h12v6M4 8h16a2 2 0 0 1 2 2v6h-4v4H6v-4H2v-6a2 2 0 0 1 2-2zM6 14h12"/></svg>
        </div>
        <div class="value">888-304-2918</div>
      </div>
      <div class="contact-row">
        <div class="icon-cell">
          <svg width="18" height="14" viewBox="0 0 24 18" aria-label="Email"><rect x="1" y="1" width="22" height="16" fill="none" stroke="#fff" stroke-width="2"/><path d="M1 1l11 9 11-9" fill="none" stroke="#fff" stroke-width="2"/></svg>
        </div>
        <div class="value">mhale@pinecrestmortgage.example</div>
      </div>
      <div class="contact-row">
        <div class="icon-cell">
          <svg width="16" height="16" viewBox="0 0 24 24" aria-label="Website"><g fill="none" stroke="#fff" stroke-width="2"><circle cx="12" cy="12" r="10"/><ellipse cx="12" cy="12" rx="4.5" ry="10"/><path d="M2 12h20M4 6.5h16M4 17.5h16"/></g></svg>
        </div>
        <div class="value">mhalepinecrestmortgage.example</div>
      </div>
      <div class="contact-row address">
        <div class="icon-cell">
          <svg width="14" height="18" viewBox="0 0 18 24" aria-label="Address"><path fill="#fff" d="M9 0a9 9 0 0 0-9 9c0 6.8 9 15 9 15s9-8.2 9-15a9 9 0 0 0-9-9zm0 12.5A3.5 3.5 0 1 1 9 5.5a3.5 3.5 0 0 1 0 7z"/></svg>
        </div>
        <div class="value">18 Larkin Ave<br>Alder Cove, DE 08614</div>
      </div>
    </div>
  </section>

</main>
</body>
</html>
```